Accident Law Firm Billboard Bold Easy to See Car Accidents

We need a billboard design that can catch attention in a very crowed Car Accident lawyer market. We wish to feature the phone number (652) 318-4470 as the focus of the Bill Board. We are trying to get the phone number recognized and remembered by drivers. The law firm name is not as crucial to remember.
Basically, It's CAR ACCIDENT? Then (652) 318-4470. We are not married to any specific color scheme but it has to POP and catch attention.
So the Crucial elements are as follows:
1. Phone number (652) 318-4470
2. Words CAR ACCIDENT?
3. Firm Logo in lower portion or where appropriate. Firm Logo to be provided
4. We may want to try a Day Glow orange color, with White and Black added. An example of the color scheme shall be provided.
5. Possible "Catch Phrase" to be used, "It's Time Call 9"
Target Market(s)
Orlando Florida Car Accident victims
Industry/Entity Type
Law Firm
Requirements
Must have
- Easy to see phone number (652) 318-4470
- Catch attention
Nice to have
- I would like to have the sign visible in bright sunlight and it not too hard to immediately know what phone number is for
Should not have
- too many words
- No bold enough
- confusing fonts
- Unclear fonts

```html
<!DOCTYPE html>
<html lang="en">
<head>
<meta charset="utf-8">
<title>Car Accident Billboard</title>
<link rel="stylesheet" href="https://fonts.googleapis.com/css2?family=Alfa+Slab+One&family=Exo+2:ital,wght@1,900&family=Rubik+Mono+One&display=swap">
<style>
  :root {
    --sky-light: #d6d6d6;
    --sky-mid: #bdbdbd;
    --swoosh-dark: #8c8c8c;
    --swoosh-deep: #6f6f6f;
    --ink: #111111;
    --paper: #ffffff;
    --dayglow: #ff9a2e;
    --dial-light: #e9e9e9;
    --dial-dark: #9a9a9a;
  }
  html, body {
    margin: 0;
    padding: 0;
    overflow: hidden;
    background: var(--sky-light);
  }
  .billboard {
    position: relative;
    width: 1200px;
    height: 350px;
    overflow: hidden;
  }
  .billboard svg { display: block; }
  .headline {
    font-family: "Rubik Mono One", "Arial Black", sans-serif;
    font-size: 136px;
    fill: var(--paper);
    stroke: var(--ink);
    stroke-width: 8px;
    paint-order: stroke fill;
    stroke-linejoin: round;
  }
  .tagline {
    font-family: "Alfa Slab One", Georgia, serif;
    font-size: 50px;
    fill: var(--ink);
    stroke: var(--paper);
    stroke-width: 6px;
    paint-order: stroke fill;
    stroke-linejoin: round;
  }
  .phone-number,
  .phone-halo {
    font-family: "Exo 2", "Arial Black", sans-serif;
    font-style: italic;
    font-weight: 900;
    font-size: 160px;
    stroke-linejoin: round;
  }
  .phone-number {
    fill: var(--dayglow);
    stroke: var(--ink);
    stroke-width: 5px;
    paint-order: stroke fill;
  }
  .phone-halo {
    fill: none;
    stroke: var(--paper);
    stroke-width: 16px;
  }
  .firm-name {
    font-family: "Rubik Mono One", "Arial Black", sans-serif;
    fill: var(--ink);
  }
  .firm-name__main { font-size: 32px; }
  .firm-name__sub { font-size: 21px; }
</style>
</head>
<body>
<main class="billboard">
  <svg width="1200" height="350" viewBox="0 0 1200 350" aria-labelledby="billboard-title">
    <title id="billboard-title">Car accident? Hurt? Call us today — (652) 318-4470, Marlowe Law Firm P.C.</title>
    <defs>
      <linearGradient id="sky" x1="0" y1="0" x2="0" y2="1">
        <stop offset="0" stop-color="var(--sky-light)"/>
        <stop offset="1" stop-color="var(--sky-mid)"/>
      </linearGradient>
      <linearGradient id="swoosh" x1="0" y1="0" x2="1" y2="0">
        <stop offset="0" stop-color="var(--swoosh-deep)"/>
        <stop offset="1" stop-color="var(--swoosh-dark)"/>
      </linearGradient>
      <radialGradient id="dial" cx="0.5" cy="0.5" r="0.5">
        <stop offset="0" stop-color="var(--dial-light)"/>
        <stop offset="1" stop-color="var(--dial-dark)" stop-opacity="0"/>
      </radialGradient>
    </defs>

    <rect class="backdrop" width="1200" height="350" fill="url(#sky)"/>
    <path class="swoosh" d="M0 215 C 300 175, 700 160, 1200 165 L1200 350 L0 350 Z" fill="url(#swoosh)"/>
    <path class="swoosh-edge" d="M0 325 C 400 305, 800 305, 1200 255 L1200 350 L0 350 Z" fill="var(--sky-mid)" opacity="0.55"/>

    <rect class="dial-artwork" role="img" aria-label="Speedometer-style clock dial with red hand" x="830" y="125" width="260" height="180" rx="90" fill="url(#dial)"/>

    <text class="headline" x="30" y="122" textLength="1080" lengthAdjust="spacingAndGlyphs">CAR ACCIDENT</text>

    <text class="tagline" x="262" y="172" textLength="540" lengthAdjust="spacingAndGlyphs">Hurt? Call Us Today</text>

    <text class="phone-halo" x="54" y="330" textLength="1020" lengthAdjust="spacingAndGlyphs" aria-hidden="true">(652) 318-4470</text>
    <text class="phone-number" x="54" y="330" textLength="1020" lengthAdjust="spacingAndGlyphs">(652) 318-4470</text>

    <g class="firm-name" transform="translate(1134 328) rotate(-90)">
      <text class="firm-name__main" x="0" y="0" textLength="214" lengthAdjust="spacingAndGlyphs">MARLOWE</text>
      <text class="firm-name__sub" x="0" y="24" textLength="214" lengthAdjust="spacingAndGlyphs">LAW FIRM P.C.</text>
    </g>
  </svg>
</main>
</body>
</html>
```